Sports League Registration Banner for plimzo

I have a graphic with a basic idea for an ad that I would like to post on plimzo but I need it to be reconfigured to fit their dimensions (1194 by 624, or in that ratio) and to have the text moved and placed in another spot on the ad. I also want the colors to be changed to look like my website (www.tarvoactive.com) but no logo on the ad. This is to promote registration for a sports league.

The idea is basically to get up off the couch and play some sports. The text on the bottom should be moved off to the side and replaced with:

GET FIT HAVE FUN
10 Game Season + Playoffs
1 Game per week
Team Fee $1525
Player Fee $125

Men's Ball Hockey

```html
<!DOCTYPE html>
<html lang="en">
<head>
<meta charset="utf-8">
<title>Men's Ball Hockey Registration</title>
<link href="https://fonts.googleapis.com/css2?family=Oswald:wght@500;600;700&display=swap" rel="stylesheet">
<style>
  :root {
    --ray-light: #a3d483;
    --ray-dark: #8fc76c;
    --glow: rgba(190, 230, 160, 0.55);
    --headline: #ffffff;
    --ink: #262626;
    --frame: #f1f1ec;
    --frame-edge: #cfcfc6;
    --accent: #6cb33f;
    --url: #3a3a3a;
    --photo-warm: #8a6a4c;
    --photo-dark: #3b3430;
  }
  * { margin: 0; padding: 0; box-sizing: border-box; }
  html, body { width: 1200px; height: 627px; overflow: hidden; }
  body { font-family: "Oswald", "Arial Narrow", sans-serif; }

  .banner {
    position: relative;
    width: 1200px;
    height: 627px;
    overflow: hidden;
    background:
      radial-gradient(circle at 560px 330px, var(--glow) 0, rgba(190,230,160,0) 520px),
      repeating-conic-gradient(from 0deg at 560px 330px,
        var(--ray-light) 0deg 7deg, var(--ray-dark) 7deg 14deg);
  }

  .snapshot {
    position: absolute;
    left: 64px;
    top: 72px;
    width: 590px;
    height: 456px;
    background: var(--frame);
    border: 1px solid var(--frame-edge);
    box-shadow: 2px 4px 10px rgba(0,0,0,0.3);
    transform: rotate(-4deg);
  }
  .snapshot__photo {
    position: absolute;
    left: 22px;
    top: 22px;
    right: 22px;
    bottom: 84px;
    background:
      radial-gradient(ellipse at 30% 45%, #c89a6a 0, rgba(200,154,106,0) 45%),
      linear-gradient(135deg, var(--photo-warm) 0%, #5e4a3c 50%, var(--photo-dark) 100%);
  }
  .snapshot__url {
    position: absolute;
    right: 24px;
    bottom: 46px;
    font-weight: 600;
    font-size: 17px;
    color: var(--url);
    letter-spacing: 0.3px;
  }
  .snapshot__deadline {
    position: absolute;
    right: 24px;
    bottom: 10px;
    font-weight: 700;
    font-size: 29px;
    color: var(--accent);
    text-transform: uppercase;
  }

  .badge {
    position: absolute;
    left: 52px;
    top: 398px;
    width: 200px;
    height: 200px;
  }
  .badge__text {
    position: absolute;
    inset: 0;
    display: flex;
    flex-direction: column;
    align-items: center;
    justify-content: center;
    font-weight: 700;
    font-size: 33px;
    line-height: 0.95;
    color: var(--ink);
    text-transform: uppercase;
    transform: rotate(-8deg);
  }

  .pointer {
    position: absolute;
    left: 640px;
    top: 350px;
    width: 70px;
    height: 110px;
  }

  .offer {
    position: absolute;
    left: 718px;
    top: 72px;
    list-style: none;
  }
  .offer__headline {
    font-weight: 700;
    font-size: 46px;
    color: var(--headline);
    text-transform: uppercase;
    text-shadow: 1px 2px 3px rgba(0,0,0,0.35);
    margin-bottom: 26px;
  }
  .offer__item {
    font-weight: 600;
    font-size: 34px;
    color: var(--ink);
    line-height: 1;
    margin-bottom: 40px;
  }
</style>
</head>
<body>
<main class="banner">
  <figure class="snapshot">
    <div class="snapshot__photo" role="img" aria-label="Photo of a man on a couch with a beer and a burger beside an old television"></div>
    <p class="snapshot__url">www.tarvoactive.com</p>
    <p class="snapshot__deadline">Registration ends April 25th</p>
  </figure>

  <div class="badge">
    <svg width="200" height="200" viewBox="0 0 200 200">
      <polygon fill="#ffffff" stroke="#9a9a9a" stroke-width="2"
        points="100,6 110,30 128,10 132,36 154,22 150,48 176,42 164,66 192,68 172,88 196,100 172,112 192,132 164,134 176,158 150,152 154,178 132,164 128,190 110,170 100,194 90,170 72,190 68,164 46,178 50,152 24,158 36,134 8,132 28,112 4,100 28,88 8,68 36,66 24,42 50,48 46,22 68,36 72,10 90,30"/>
    </svg>
    <div class="badge__text"><span>It's</span><span>Never</span><span>Too</span><span>Late</span></div>
  </div>

  <svg class="pointer" viewBox="0 0 70 110" fill="none" stroke="#4a3a30" stroke-width="2.5" stroke-linecap="round">
    <path d="M56 4 C30 8 34 30 48 34 C60 38 52 20 40 28 C22 40 30 70 38 100"/>
    <path d="M28 90 L38 102 L46 88"/>
  </svg>

  <ul class="offer">
    <li class="offer__headline">Get Fit Have Fun!</li>
    <li class="offer__item">10 Game Season + Playoffs</li>
    <li class="offer__item">1 Game per week</li>
    <li class="offer__item">Team Fee $1525</li>
    <li class="offer__item">Player Fee $125</li>
  </ul>
</main>
</body>
</html>
```